Marlo’s Sandwich Corner Grand Opening Door Flyer

1. Project Title
• “Flyer Design for Sandwich Shop Grand Opening”
• Why it’s effective: Direct and to the point, highlighting the purpose of the design.

2. Project Description
• “We’re looking for a professional designer to create a vibrant and modern flyer for our sandwich shop, Marlo’s Corner. The flyer should emphasize our handcrafted sandwiches, fresh-baked bread, and house-made meats. As a women & family-owned business, we want this aspect prominently displayed. The flyer should also include our logo, a ‘Grand Opening’ and our website: MarlosCorner.com. We want the design to be clean, bold, and visually appealing to attract customers. We also would like a QR code so they can scan to load of the website to order online, but also list it.
• Why it’s effective: Clear goals, modern style preference, and necessary details outlined.

3. Visual Style
• “Modern, bold, and clean design with bright, appetizing colors. Focus on high-quality imagery of sandwiches, sleek fonts, and an inviting layout.”
• Why it’s effective: Communicates the desired aesthetic and tone.

4. Key Details to Include
• Business Name: Marlo’s Sandwich Corner
• Taglines:
“Women & Family Owned”
“Handcrafted Sandwiches Made with Love”
“Fresh Baked Bread”
“House-made Slow Roasted House Specialties”
“Gluten-Friendly”
“Vegan-Friendly”
“7:00am Fresh Daily Morning Mill Coffee and Breakfast”

• Call-to-Action: “Order Online at MarlosCorner.com”
• Placeholder for the logo.
• Size: 4.25 x 11 (Door Hanger)
• File Format: High-resolution PDF, JPEG, or PNG.
• Print-Ready: Include bleed margins and ensure print clarity.

6. Tone
• Friendly and professional. Highlighting that your business is women-owned adds a unique and personal touch vs deli meat shops. We are a gourmet sandwich shop, with fresh baked bread, house-made meats, with gluten and vegan options. Each sandwich is made with love.

Target Market(s)

Coffee drinkers for morning crowd and sandwiches for lunch

Industry/Entity Type

Sandwich Shop

Colors
EB3D1F
EC4F4E
F09395
F8D3D4
FCEDEE

Requirements
Must have
• See Description
Nice to have
• Use website to get a feel for color theme
Should not have
• NA

```html
<!DOCTYPE html>
<html lang="en">
<head>
<meta charset="utf-8">
<title>Marlo’s Sandwich Corner – Door Hanger</title>
<link rel="stylesheet" href="https://fonts.googleapis.com/css2?family=Oswald:wght@400;500&family=Pacifico&family=Rubik:wght@800;900&family=Paytone+One&display=swap">
<style>
  :root{
    --red:#EB3D1F;
    --coral:#EC4F4E;
    --rose:#F09395;
    --blush:#F8D3D4;
    --mist:#FCEDEE;
    --white:#ffffff;
    --ink:#000000;
  }
  *{box-sizing:border-box;margin:0;padding:0}
  html,body{width:1200px;height:1200px;overflow:hidden;background:var(--white)}
  .canvas{position:relative;width:1200px;height:1200px;background:var(--white)}
  .hanger{position:absolute;top:60px;width:426px;height:1080px;overflow:hidden;
    background:radial-gradient(ellipse at 50% 55%, var(--white) 0%, var(--mist) 45%, var(--blush) 100%)}
  .hanger--front{left:136px}
  .hanger--back{left:644px;width:424px}
  .abs{position:absolute}
  .center{left:0;right:0;text-align:center}
  .door-hole{position:absolute;background:var(--ink);border-radius:130px 130px 0 0}

  /* front */
  .front-top{position:absolute;left:0;top:0;width:100%;height:372px}
  .tagline-small{top:22px;font:500 16px/1 "Oswald",sans-serif;color:var(--white);letter-spacing:1px}
  .icon{position:absolute;width:40px;height:40px}
  .open-line{display:flex;justify-content:center;align-items:baseline;gap:6px;height:76px;
    line-height:1;white-space:nowrap;color:var(--white)}
  .open-script{font:400 42px/1 "Pacifico",cursive}
  .open-word{font:400 72px/1 "Paytone One",sans-serif;letter-spacing:1px}
  .headline{left:24px;top:388px;font:400 34px/1.2 "Oswald",sans-serif;color:var(--red);text-transform:uppercase}
  .love{left:186px;top:424px;font:400 66px/1 "Pacifico",cursive;color:var(--white);
    -webkit-text-stroke:3px var(--red);paint-order:stroke fill;transform:rotate(-8deg)}
  .fresh-badge{left:38px;top:500px;width:120px;height:120px;border-radius:50%;background:var(--red);
    display:flex;align-items:center;justify-content:center;text-align:center;
    font:900 18px/1.15 "Rubik",sans-serif;color:var(--white);z-index:2}
  .photo{position:absolute;border-radius:60px 60px 40px 40px/70px 70px 40px 40px}
  .photo--front{left:10px;top:582px;width:406px;height:206px;
    background:linear-gradient(180deg,#d9a46a 0%,#b5773f 35%,#6b3f26 52%,#c9493a 68%,#e9d9b8 100%)}
  .specialties{top:806px;font:900 30px/1.06 "Rubik",sans-serif;color:var(--red);text-transform:uppercase;
    -webkit-text-stroke:6px var(--white);paint-order:stroke fill}
  .front-foot{position:absolute;left:0;bottom:0;width:100%;height:160px;background:var(--blush)}
  .brand{font-family:"Rubik",sans-serif;font-weight:900;color:var(--red);text-align:center;line-height:1}
  .brand-name{font-size:62px}
  .brand-sub{font-size:18px;letter-spacing:2px;margin-top:4px;text-transform:uppercase}
  .front-brand{top:936px}
  .front-url{top:1040px;font:400 22px/1 "Oswald",sans-serif;color:var(--red);text-transform:uppercase}

  /* back */
  .badge{position:absolute;width:92px;height:92px;border-radius:50%;background:var(--red);
    display:flex;align-items:center;justify-content:center;text-align:center;
    font:800 12px/1.1 "Rubik",sans-serif;color:var(--white);text-transform:uppercase}
  .back-open{top:266px;color:var(--red)}
  .hours-box{position:absolute;left:34px;top:350px;width:356px;height:70px;border:2px dashed var(--red);
    border-radius:10px;background:var(--white);text-align:center;color:var(--red);padding-top:6px}
  .hours-main{font:400 25px/1.2 "Oswald",sans-serif;text-transform:uppercase}
  .hours-sub{font:400 17px/1.2 "Oswald",sans-serif;text-transform:uppercase;letter-spacing:.5px}
  .back-band{position:absolute;left:0;top:446px;width:100%;height:292px}
  .back-brand{top:482px}
  .back-brand .brand-name,.back-brand .brand-sub{color:var(--blush)}
  .photo--back{left:10px;top:610px;width:408px;height:156px;
    background:linear-gradient(180deg,#d8b98a 0%,#c89c63 28%,#b9d06a 40%,#d97a74 55%,#f1d27a 72%,#d3a86d 100%)}
  .motto-icons{position:absolute;left:0;top:776px;width:100%;height:60px}
  .motto{top:850px;font:500 15px/1 "Oswald",sans-serif;color:var(--coral);letter-spacing:3px;text-transform:uppercase}
  .back-foot{position:absolute;left:0;bottom:0;width:100%;height:196px}
  .owned{top:910px;font:400 25px/1.2 "Pacifico",cursive;color:var(--white)}
  .family-badge{position:absolute;left:40px;top:952px;width:100px;height:100px;border-radius:50%;
    background:var(--red);border:3px solid var(--white);box-shadow:inset 0 0 0 6px var(--red),inset 0 0 0 8px var(--white)}
  .order-label{position:absolute;left:160px;width:250px;top:962px;text-align:center;
    font:500 25px/1 "Oswald",sans-serif;color:var(--white);text-transform:uppercase}
  .url-cloud{position:absolute;left:190px;top:996px}
  .back-url{position:absolute;left:160px;width:250px;top:1044px;text-align:center;
    font:400 23px/1 "Oswald",sans-serif;color:var(--white);text-transform:uppercase}
</style>
</head>
<body>
<main class="canvas">

  <section class="hanger hanger--front" aria-label="Door hanger front">
    <svg class="front-top" viewBox="0 0 426 372" preserveAspectRatio="none" aria-hidden="true">
      <path d="M0 0H426V354Q405 372 384 354T341 354T298 354T256 354T213 354T170 354T128 354T85 354T42 354T0 354Z" fill="var(--red)"/>
    </svg>
    <div class="door-hole" style="left:78px;top:46px;width:270px;height:220px"></div>
    <p class="abs center tagline-small">PEACE + LOVE</p>

    <svg class="icon" style="left:22px;top:46px" viewBox="0 0 24 24" aria-hidden="true"><g fill="none" stroke="var(--white)" stroke-width="1.3"><circle cx="12" cy="12" r="10"/><path d="M12 2V22M12 12L5 19M12 12L19 19"/></g></svg>
    <svg class="icon" style="left:22px;top:110px" viewBox="0 0 24 24" aria-hidden="true"><path d="M12 21s-7-4.5-9.5-9A5 5 0 0 1 12 6a5 5 0 0 1 9.5 6C19 16.5 12 21 12 21z" fill="none" stroke="var(--white)" stroke-width="1.3"/></svg>
    <svg class="icon" style="left:22px;top:172px" viewBox="0 0 24 24" aria-hidden="true"><g fill="none" stroke="var(--white)" stroke-width="1.3"><circle cx="12" cy="12" r="10"/><path d="M12 2V22M12 12L5 19M12 12L19 19"/></g></svg>
    <svg class="icon" style="left:22px;top:234px" viewBox="0 0 24 24" aria-hidden="true"><path d="M12 21s-7-4.5-9.5-9A5 5 0 0 1 12 6a5 5 0 0 1 9.5 6C19 16.5 12 21 12 21z" fill="none" stroke="var(--white)" stroke-width="1.3"/></svg>
    <svg class="icon" style="left:364px;top:46px" viewBox="0 0 24 24" aria-hidden="true"><path d="M12 21s-7-4.5-9.5-9A5 5 0 0 1 12 6a5 5 0 0 1 9.5 6C19 16.5 12 21 12 21z" fill="none" stroke="var(--white)" stroke-width="1.3"/></svg>
    <svg class="icon" style="left:364px;top:110px" viewBox="0 0 24 24" aria-hidden="true"><g fill="none" stroke="var(--white)" stroke-width="1.3"><circle cx="12" cy="12" r="10"/><path d="M12 2V22M12 12L5 19M12 12L19 19"/></g></svg>
    <svg class="icon" style="left:364px;top:172px" viewBox="0 0 24 24" aria-hidden="true"><path d="M12 21s-7-4.5-9.5-9A5 5 0 0 1 12 6a5 5 0 0 1 9.5 6C19 16.5 12 21 12 21z" fill="none" stroke="var(--white)" stroke-width="1.3"/></svg>
    <svg class="icon" style="left:364px;top:234px" viewBox="0 0 24 24" aria-hidden="true"><g fill="none" stroke="var(--white)" stroke-width="1.3"><circle cx="12" cy="12" r="10"/><path d="M12 2V22M12 12L5 19M12 12L19 19"/></g></svg>

    <h1 class="abs center open-line" style="top:272px"><span class="open-script">We are</span><span class="open-word">OPEN</span></h1>

    <p class="abs headline">Handcrafted sandwiches<br>made with</p>
    <p class="abs love">Love</p>

    <div class="abs fresh-badge">FRESH<br>BAKED<br>BREAD</div>
    <div class="photo photo--front" role="img" aria-label="Photo of a toasted seeded roll filled with grilled beef patties, lettuce and tomato"></div>

    <p class="abs center specialties">House-made<br>Slow roasted<br>House specialties</p>

    <div class="front-foot"></div>
    <div class="abs center brand front-brand">
      <div class="brand-name">Marlo’s</div>
      <div class="brand-sub">Sandwich Corner</div>
    </div>
    <p class="abs center front-url">Order online at MarlosCorner.com</p>
  </section>

  <section class="hanger hanger--back" aria-label="Door hanger back">
    <div class="door-hole" style="left:84px;top:46px;width:268px;height:212px"></div>
    <div class="badge" style="left:4px;top:-4px">Gluten<br>Friendly</div>
    <div class="badge" style="left:332px;top:-8px">Vegan<br>Friendly</div>

    <h2 class="abs center open-line back-open"><span class="open-script">We are</span><span class="open-word">OPEN</span></h2>

    <div class="hours-box">
      <p class="hours-main">✦ 7:00 AM Fresh Daily ✦</p>
      <p class="hours-sub">Morning Mill Coffee &amp; Breakfast</p>
    </div>

    <svg class="back-band" viewBox="0 0 424 292" preserveAspectRatio="none" aria-hidden="true">
      <path d="M0 48L424 0V292H0Z" fill="var(--red)"/>
    </svg>
    <div class="abs center brand back-brand">
      <div class="brand-name">Marlo’s</div>
      <div class="brand-sub">Sandwich Corner</div>
    </div>
    <div class="photo photo--back" role="img" aria-label="Photo of a ciabatta sandwich with ham, cheese, tomato, cucumber and lettuce"></div>

    <svg class="motto-icons" viewBox="0 0 424 60" aria-hidden="true">
      <g fill="none" stroke="var(--coral)" stroke-width="2">
        <circle cx="92" cy="30" r="25"/><path d="M92 5V55M92 30L74 48M92 30L110 48"/>
        <path d="M188 56s-24-14-29-28a14 14 0 0 1 29-9a14 14 0 0 1 29 9c-5 14-29 28-29 28z"/>
        <path d="M270 22Q305 0 340 22Z"/><path d="M270 31Q279 25 288 31T305 31T322 31T340 31"/><path d="M270 42H340"/><path d="M270 48Q305 58 340 48"/>
      </g>
    </svg>
    <p class="abs center motto">Peace ✦ Love ✦ Sandwiches</p>

    <svg class="back-foot" viewBox="0 0 424 196" preserveAspectRatio="none" aria-hidden="true">
      <path d="M0 16Q21 0 42 16T85 16T127 16T170 16T212 16T254 16T297 16T339 16T382 16T424 16V196H0Z" fill="var(--red)"/>
    </svg>
    <p class="abs center owned">Women &amp; Family Owned</p>
    <div class="family-badge"></div>
    <p class="order-label">Order online at</p>
    <svg class="url-cloud" width="190" height="44" viewBox="0 0 190 44" aria-hidden="true">
      <path d="M0 44V30Q0 6 24 6Q40 6 47 18Q55 0 80 0Q100 0 108 16Q116 4 134 4Q152 4 158 18Q166 10 176 12Q190 16 190 32V44Z" fill="var(--blush)"/>
    </svg>
    <p class="back-url">MarlosCorner.com</p>
  </section>

</main>
</body>
</html>
```